Create a "germ free" Poster Design Project

Hi we're a media business who sells advertising space on a unique dispensing device that also sanitizes your hands.

I'm looking for a poster design that highlights the need to sanitize hands which removes 99.9% of germs and also promotes a healthy & clean lifestyle.
(you may want to use kid friendly images of bugs to highlight germs)
Whilst the primary message will be to sanitize your hands the secondary message is also to "use this space" to advertise on.

The poster should be colorful yet simple and not too wordy.

Thanks

Target Market(s)

General cunsumer public but more specifically women and moms

Industry/Entity Type

Advertising

Requirements
Must have
• A central picture (animated or real) to highlight the practice of sanitizing hands (or removing germs)
Perhaps an arrow down to invite consumers to "try it now, its free'
Nice to have
• Referal to our web site: Plorvex.com.au (currently not operational) and email info@plorvex.com.au
Perhaps an image of a baby's hand with a creative tag line.
Should not have
• Nothing too gross looking

```html
<!DOCTYPE html>
<html lang="en">
<head>
<meta charset="utf-8">
<title>Germ Free Poster</title>
<link href="https://fonts.googleapis.com/css2?family=Cabin:wght@500;600;700&display=swap" rel="stylesheet">
<style>
  :root {
    --paper: #f3f0e7;
    --ink: #464646;
    --accent: #d9694a;
    --banner-top: #ec8a65;
    --banner-bottom: #b6472d;
    --banner-text: #f4ebdc;
    --green: #3f8f5f;
    --green-dark: #2f6f48;
    --btn-top: #4f9b68;
    --btn-bottom: #2f6c45;
    --page: #e7e4dc;
  }
  * { margin: 0; padding: 0; box-sizing: border-box; }
  html, body { width: 1200px; height: 900px; overflow: hidden; background: var(--page); }
  body { font-family: "Cabin", "Trebuchet MS", sans-serif; }

  .poster {
    position: relative;
    width: 1200px;
    height: 900px;
    background: var(--paper);
    overflow: hidden;
  }

  .stripe {
    position: absolute;
    left: 0;
    width: 100%;
    height: 38px;
    display: flex;
  }
  .stripe--top { top: 0; }
  .stripe--bottom { bottom: 0; height: 34px; }
  .stripe span { flex: 1; }
  .c1 { background: #4f8f74; }
  .c2 { background: #7ec8cc; }
  .c3 { background: #6aa5b0; }
  .c4 { background: #7d96a3; }
  .c5 { background: #3f7c80; }
  .c6 { background: #79c3cc; }
  .c7 { background: #3a3f44; }
  .c8 { background: #9a9e83; }
  .c9 { background: #8fbcd0; }
  .c10 { background: #4c7a9e; }

  .headline {
    position: absolute;
    top: 38px;
    left: 0;
    width: 100%;
    height: 212px;
    background: var(--paper);
    box-shadow: 0 4px 8px rgba(0,0,0,0.18);
    z-index: 3;
    color: var(--ink);
    font-weight: 700;
    text-align: right;
    padding-right: 48px;
  }
  .headline__warning {
    position: absolute;
    right: 48px;
    top: 52px;
    font-size: 36px;
    letter-spacing: 0.3px;
    white-space: nowrap;
  }
  .headline__warning em {
    font-style: normal;
    color: var(--accent);
    font-size: 48px;
  }
  .headline__claim {
    position: absolute;
    right: 56px;
    top: 126px;
    font-size: 42px;
    white-space: nowrap;
  }
  .headline__claim em {
    font-style: normal;
    color: var(--accent);
    font-size: 58px;
  }

  .hero {
    position: absolute;
    left: 0;
    top: 200px;
    width: 680px;
    height: 666px;
    z-index: 1;
  }

  .cta-banner {
    position: absolute;
    left: 685px;
    top: 250px;
    width: 465px;
    height: 346px;
    z-index: 2;
  }
  .cta-banner svg { position: absolute; inset: 0; }
  .cta-banner__text {
    position: absolute;
    left: 0;
    width: 100%;
    text-align: center;
    color: var(--banner-text);
    font-weight: 700;
    text-shadow: 0 2px 3px rgba(0,0,0,0.25);
    white-space: nowrap;
  }
  .cta-banner__try { top: 34px; font-size: 56px; }
  .cta-banner__free { top: 108px; font-size: 84px; }

  .advertise-label {
    position: absolute;
    left: 694px;
    width: 472px;
    top: 642px;
    text-align: center;
    font-size: 30px;
    font-weight: 500;
    color: var(--ink);
  }

  .contact-button {
    position: absolute;
    left: 694px;
    top: 724px;
    width: 472px;
    height: 118px;
    border-radius: 10px;
    background: linear-gradient(var(--btn-top), var(--btn-bottom));
    box-shadow: 0 3px 5px rgba(0,0,0,0.25);
    color: #fff;
    text-align: center;
    font-weight: 700;
    padding-top: 18px;
  }
  .contact-button__site { font-size: 34px; line-height: 42px; }
  .contact-button__email { font-size: 27px; line-height: 38px; }
</style>
</head>
<body>
<main class="poster">
  <div class="stripe stripe--top">
    <span class="c1"></span><span class="c2"></span><span class="c3"></span><span class="c4"></span><span class="c5"></span>
    <span class="c6"></span><span class="c7"></span><span class="c8"></span><span class="c9"></span><span class="c10"></span>
  </div>

  <header class="headline">
    <p class="headline__warning">Sometimes Hand Wash is Just <em>NOT</em> Enough to kill them!!</p>
    <p class="headline__claim">Use Sanitizer. Kill <em>99.9%</em> Germs.</p>
  </header>

  <svg class="hero" viewBox="0 200 680 666" role="img" aria-label="Photo of a young boy washing his hands at a kitchen sink, with a cartoon speech burst full of grumpy germ characters">
    <defs>
      <linearGradient id="heroTones" x1="0" y1="0" x2="1" y2="1">
        <stop offset="0" stop-color="#c9d3da"/>
        <stop offset="0.5" stop-color="#8e969c"/>
        <stop offset="1" stop-color="#5d6469"/>
      </linearGradient>
      <clipPath id="heroClip">
        <circle cx="175" cy="715" r="470"/>
      </clipPath>
    </defs>
    <rect x="0" y="200" width="680" height="666" fill="url(#heroTones)" clip-path="url(#heroClip)"/>
    <circle cx="175" cy="715" r="470" fill="none" stroke="var(--green)" stroke-width="12"/>
  </svg>

  <div class="cta-banner">
    <svg viewBox="0 0 465 346" width="465" height="346" aria-hidden="true">
      <defs>
        <linearGradient id="bannerFill" x1="0" y1="0" x2="0" y2="1">
          <stop offset="0" stop-color="var(--banner-top)"/>
          <stop offset="1" stop-color="var(--banner-bottom)"/>
        </linearGradient>
      </defs>
      <path d="M0 0 H465 V222 L232 346 L0 222 Z" fill="url(#bannerFill)"/>
    </svg>
    <p class="cta-banner__text cta-banner__try">Try it NOW!</p>
    <p class="cta-banner__text cta-banner__free">It’s FREE!</p>
  </div>

  <p class="advertise-label">Use This Space To Advertise:</p>

  <div class="contact-button">
    <p class="contact-button__site">Plorvex.com.au</p>
    <p class="contact-button__email">Info: info@plorvex.com.au</p>
  </div>

  <div class="stripe stripe--bottom">
    <span class="c1"></span><span class="c2"></span><span class="c3"></span><span class="c4"></span><span class="c5"></span>
    <span class="c6"></span><span class="c7"></span><span class="c8"></span><span class="c9"></span><span class="c10"></span>
  </div>
</main>
</body>
</html>
```